Korvane Sky Works, LLC - Business Card

I currently have a drone business that specializes in aerial photography, thermal image inspections, deer recovery, search and rescue, custom agricultural applications. i will attach my current business card as well as some logos to incorporate for a new up to date business card
Updates

Designs look the same

Sick

Target Market(s)

farmers, hunters

Contact Information for Business Card

name address phone number (as existing card i attached)

Requirements
Must have
• im good with existing business card, but would like an agricultural twist

```html
<!DOCTYPE html>
<html lang="en">
<head>
<meta charset="utf-8">
<title>Korvane Sky Works, LLC – Business Card</title>
<link href="https://fonts.googleapis.com/css2?family=Roboto+Condensed:wght@400;700&family=Roboto:wght@400;700&display=swap" rel="stylesheet">
<style>
  :root{
    --backdrop:#3d3d3d;
    --green-light:#5a9e22;
    --green:#3a8a16;
    --green-dark:#1f700c;
    --white:#ffffff;
    --shadow-grey:#8a8a8a;
  }
  *{box-sizing:border-box;margin:0;padding:0}
  html,body{width:1200px;height:803px;overflow:hidden;background:var(--backdrop)}
  .stage{position:relative;width:1200px;height:803px;display:flex;align-items:center;justify-content:center;gap:40px}
  .card{position:relative;width:540px;height:310px;border-radius:22px;overflow:hidden;box-shadow:0 14px 30px rgba(0,0,0,.45)}

  /* Front */
  .card--front{background:var(--white)}
  .front-art{position:absolute;inset:0}
  .contact{position:absolute;left:40px;top:62px;color:var(--white);font-family:"Roboto",sans-serif}
  .contact__name{font-family:"Roboto Condensed",sans-serif;font-size:26px;font-weight:400;letter-spacing:.5px}
  .contact__name b{font-weight:700}
  .contact__role{font-size:13px;margin-top:2px}
  .contact__address{font-size:13px;line-height:17px;margin-top:24px}
  .contact__list{list-style:none;font-size:13px;line-height:18px;margin-top:16px}
  .contact__list li{display:flex;align-items:center;gap:8px}
  .contact__list svg{width:11px;height:11px;flex:none}
  .brand{position:absolute;right:48px;top:70px;width:170px;height:170px;display:flex;flex-direction:column;align-items:center;justify-content:center;border:6px solid var(--green);border-radius:50%}
  .brand__name{font-family:"Roboto Condensed",sans-serif;font-weight:700;font-size:30px;color:var(--green);letter-spacing:1px}

  /* Back */
  .card--back{background:radial-gradient(ellipse at 30% 80%,var(--green-light),var(--green) 45%,var(--green-dark))}
  .back-brand{position:absolute;left:0;right:0;top:62px;display:flex;align-items:center;justify-content:center;gap:16px}
  .back-brand__mark{width:70px;height:70px;border:7px solid var(--white);border-radius:50%}
  .back-brand__name{font-family:"Roboto Condensed",sans-serif;font-weight:700;font-size:62px;color:var(--white);letter-spacing:2px}
  .rule{position:absolute;left:50px;right:50px;height:1px;background:rgba(255,255,255,.85)}
  .rule--top{top:186px}
  .rule--bottom{top:268px}
  .services{position:absolute;left:0;right:0;top:198px;text-align:center;font-family:"Roboto Condensed",sans-serif;color:var(--white);font-size:17px;line-height:28px;letter-spacing:.3px}
  .services .dot{display:inline-block;width:8px;height:8px;border-radius:50%;background:var(--white);margin:0 10px;vertical-align:middle}
</style>
</head>
<body>
<main class="stage">
  <section class="card card--front">
    <svg class="front-art" viewBox="0 0 540 310" aria-hidden="true">
      <defs>
        <radialGradient id="frontGreen" cx="30%" cy="55%" r="70%">
          <stop offset="0" stop-color="#5a9e22"/>
          <stop offset="1" stop-color="#247a0e"/>
        </radialGradient>
      </defs>
      <circle cx="60" cy="180" r="262" fill="#8a8a8a"/>
      <circle cx="52" cy="180" r="258" fill="#ffffff"/>
      <circle cx="44" cy="180" r="256" fill="url(#frontGreen)"/>
    </svg>
    <div class="contact">
      <h1 class="contact__name">MASON <b>HALE</b></h1>
      <p class="contact__role">Owner</p>
      <p class="contact__address">214 W. Elm St.<br>Dorrance, OH 45910</p>
      <ul class="contact__list">
        <li><svg viewBox="0 0 12 12"><path d="M2 1l3 3-1.5 1.5a7 7 0 0 0 3 3L8 7l3 3-2 2C4 11 1 8 0 3z" fill="#fff"/></svg>555-014-2270</li>
        <li><svg viewBox="0 0 12 12"><rect x="0" y="2" width="12" height="8" fill="#fff"/><path d="M0 2l6 5 6-5" stroke="#3a8a16" fill="none"/></svg>korvanesky@mail.com</li>
        <li><svg viewBox="0 0 12 12"><circle cx="6" cy="6" r="5.5" fill="#fff"/></svg>www.korvaneskyworks.com</li>
      </ul>
    </div>
    <div class="brand">
      <span class="brand__name">KORVANE</span>
    </div>
  </section>

  <section class="card card--back">
    <div class="back-brand">
      <span class="back-brand__mark"></span>
      <span class="back-brand__name">KORVANE</span>
    </div>
    <div class="rule rule--top"></div>
    <p class="services">
      THERMAL IMAGE INSPECTIONS<span class="dot"></span>DEER RECOVERY<br>
      SEARCH&amp; RESCUE<span class="dot"></span>REAL ESTATE PHOTOGRAPHY
    </p>
    <div class="rule rule--bottom"></div>
  </section>
</main>
</body>
</html>
```